Corporate flyer introducing a brand new technology apprenticeship program in Australia!

A professional, yet clean and contemporary looking flyer to advertise a brand new service offering in a simple, easy to read format with engaging images. Here is a link to our current online brochure which outlines the program we would like to advertise in a hardcopy flyer/brochure format: https://pages.vendrap.com/Information-on-Technology-Higher-Apprenticeships-for-Employers-Victoria-kT3pzqW7LmRe

Target Market(s)

Medium to large sized businesses involved in using cutting edge technology, such as engineering and advanced manufracturing (3D printing etc)

Industry/Entity Type

Engineering

Colors

Designer to choose colors to be used in the design.

Requirements
Must have
• Contemporary, clean looking, easy to read, tech/engineering/advanced manufacturing related imagery
Nice to have
• Some ideas about different sizes/styles (eg something other than a plain A4 sheet)
Should not have
• Unprofessional or offensive language

```html
<!DOCTYPE html>
<html lang="en">
<head>
<meta charset="utf-8">
<title>Technology Higher Apprentices 2019 – Spread 02/03</title>
<link href="https://fonts.googleapis.com/css2?family=Questrial&family=Didact+Gothic&display=swap" rel="stylesheet">
<style>
  :root {
    --backdrop: #e4e4e4;
    --brand-red: #c9361c;
    --paper: #f4f4f4;
    --ink: #333333;
    --ink-soft: #5a5a5a;
    --faint: #e2e2e2;
    --white: #ffffff;
  }
  * { box-sizing: border-box; margin: 0; padding: 0; }
  html, body { width: 1200px; height: 841px; overflow: hidden; background: var(--backdrop); }
  body { font-family: "Questrial", "Didact Gothic", sans-serif; }

  .spread {
    position: absolute; left: 60px; top: 150px;
    width: 1080px; height: 540px; display: flex;
    box-shadow: 0 10px 30px rgba(0,0,0,.15);
  }
  .page { position: relative; width: 540px; height: 540px; overflow: hidden; }

  /* Left page */
  .page--intro { background: var(--brand-red); color: var(--white); }
  .page--intro .page-title {
    position: absolute; left: 44px; top: 44px;
    font-size: 30px; font-weight: 400; letter-spacing: .5px;
  }
  .page--intro .body-copy {
    position: absolute; left: 44px; top: 94px; width: 460px;
    font-family: "Didact Gothic", sans-serif; font-size: 9px; line-height: 1.4;
  }
  .page--intro .body-copy p + p { margin-top: 8px; }

  .eras { position: absolute; left: 40px; top: 296px; width: 470px; height: 166px; }
  .era { position: absolute; width: 110px; }
  .era-art { width: 100%; height: 56px; border-radius: 4px;
    background: linear-gradient(180deg, rgba(255,255,255,.85), rgba(255,255,255,.6)); }
  .era-name { margin-top: 6px; font-size: 11px; font-weight: 700; }
  .era-note { margin-top: 2px; font-family: "Didact Gothic", sans-serif; font-size: 7.5px; line-height: 1.35; }
  .era--1 { left: 0;     top: 42px; }
  .era--2 { left: 118px; top: 28px; }
  .era--3 { left: 236px; top: 14px; }
  .era--4 { left: 354px; top: 0; }

  .footer { position: absolute; bottom: 26px; display: flex; align-items: baseline; gap: 14px; }
  .footer .page-number { font-size: 38px; font-weight: 400; line-height: 1; }
  .footer .running-head { font-size: 7.5px; letter-spacing: 2.5px; text-transform: uppercase; }
  .page--intro .footer { left: 36px; }
  .page--intro .page-number { color: rgba(255,255,255,.55); }

  /* Right page */
  .page--program { background: linear-gradient(90deg, #dcdcdc 0, var(--paper) 40px, var(--paper)); color: var(--ink); }
  .faint-numeral {
    position: absolute; right: -30px; bottom: -80px;
    font-size: 520px; line-height: 1; color: var(--faint); font-family: "Questrial", sans-serif;
  }
  .badge-square { position: absolute; right: 56px; top: 46px; width: 30px; height: 30px; background: var(--brand-red); }
  .program-title {
    position: absolute; left: 50px; top: 66px;
    font-size: 25px; font-weight: 400; line-height: 1.1; color: var(--brand-red);
  }
  .program-content { position: absolute; left: 50px; top: 176px; width: 440px; }
  .program-lead { font-size: 13px; font-weight: 700; line-height: 1.3; color: var(--ink); margin-bottom: 12px; }
  .program-content p.detail {
    font-family: "Didact Gothic", sans-serif; font-size: 8.5px; line-height: 1.5; color: var(--ink-soft);
  }
  .program-content p.detail + p.detail { margin-top: 8px; }
  .page--program .footer { right: 36px; }
  .page--program .running-head { color: var(--brand-red); }
  .page--program .page-number { color: #b8b8b8; }
</style>
</head>
<body>
  <main class="spread">
    <section class="page page--intro">
      <h1 class="page-title">What is Industry 4.0</h1>
      <div class="body-copy">
        <p>The term Industry 4.0 encompasses the digitalisation of production processes based on devices autonomously communicating with each other along a value chain. Production units become ‘smart factories’ where computer-driven systems monitor physical processes.</p>
        <p>Automation, sensors, cloud computing, big data analytics and machine-to-machine communication are driving new business opportunities through integration with the global supply chain. Industry 4.0 technologies make it possible to gather and analyse data across machines enabling faster, more flexible, and more efficient processes to produce higher quality goods at reduced costs.</p>
        <p>This in turn increases manufacturing productivity, shifts economics, fosters industrial growth, modifies the profile of the workforce and ultimately changes the competitiveness of companies.</p>
        <p>What does this mean for Australian businesses? Essentially it requires businesses to innovate, collaborate and redefine future parameters. Whilst innovation doesn’t necessarily transform an industry overnight, failure to build capability and develop forward thinking infrastructure has the potential to lead to irrelevance much quicker than expected.</p>
      </div>

      <div class="eras">
        <div class="era era--1">
          <div class="era-art" role="img" aria-label="Line illustration of a steam engine on rails"></div>
          <div class="era-name">Industry 1.0</div>
          <div class="era-note">The Industrial Revolution begins. Mechanization of manufacturing with the introduction of steam and water power</div>
        </div>
        <div class="era era--2">
          <div class="era-art" role="img" aria-label="Line illustration of an early motor car"></div>
          <div class="era-name">Industry 2.0</div>
          <div class="era-note">Mass production assembly lines using electrical power</div>
        </div>
        <div class="era era--3">
          <div class="era-art" role="img" aria-label="Line illustration of a robotic arm over a conveyor belt"></div>
          <div class="era-name">Industry 3.0</div>
          <div class="era-note">Automated production using electronics, programmable logic controllers (PLC), IT systems and robotics</div>
        </div>
        <div class="era era--4">
          <div class="era-art" role="img" aria-label="Line illustration of a cloud linked to devices and a robot arm"></div>
          <div class="era-name">Industry 4.0</div>
          <div class="era-note">The ‘Smart Factory’. Autonomous decision making of cyber physical systems using machine learning and Big Data analysis. Interoperability through IoT and cloud technology.</div>
        </div>
      </div>

      <footer class="footer">
        <span class="page-number">02</span>
        <span class="running-head">Technology Higher Apprentices 2019</span>
      </footer>
    </section>

    <section class="page page--program">
      <div class="faint-numeral" aria-hidden="true">4</div>
      <div class="badge-square" aria-hidden="true"></div>
      <h2 class="program-title">Industry 4.0<br>Higher Apprenticeships<br>Pilot Program</h2>
      <div class="program-content">
        <p class="program-lead">The program utilises an apprenticeship framework to deliver a new Diploma and Associate Degree in Applied Technologies.</p>
        <p class="detail">The original project is funded as a pilot by the National Skills Office, led and managed by the Industry Council, and implemented in collaboration with Kestrel Systems and Northgate University of Technology.</p>
        <p class="detail">Focusing on Industry 4.0 and the Internet of Things, IT Disruptive Technologies, Engineering, Design and Business, the course will enable employers to train future technicians with a higher skills level to meet their needs in an Industry 4.0 based economy.</p>
        <p class="detail">The pilot combines the best of university and vocational learning models to improve Science, Technology, Engineering and Math (STEM) skills of technically minded participants, incorporating skills for business and design.</p>
        <p class="detail">The hands on and worked based component ensures applicants are productive in industry whilst applying the advanced knowledge gained from the off-the-job training.</p>
      </div>
      <footer class="footer">
        <span class="running-head">Technology Higher Apprentices 2019</span>
        <span class="page-number">03</span>
      </footer>
    </section>
  </main>
</body>
</html>
```